Birchwood Clover Business Cards

I need a business card with my logo, number, Facebook account, and some information about what I am selling. Green card with logo on the front. 555-218-3946 phone number, @birchwoodclover Facebook, •Orchardgrass Hay •Alfalfa Hay •Mixed Grass Hay , and “Premium Quality Hay” all written on the back.

Target Market(s)

Hay

Contact Information for Business Card

Phone number, Facebook, different types of hay.

Colors
00AB8E
00BBA5
67D7C9
C6EFE9
E9F9F6

```html
<!DOCTYPE html>
<html lang="en">
<head>
<meta charset="utf-8">
<title>Birchwood Clover Business Cards</title>
<link href="https://fonts.googleapis.com/css2?family=Kaushan+Script&family=Arimo:wght@400;700&display=swap" rel="stylesheet">
<style>
  :root{
    --stage:#e6e6e4;
    --card-white:#f8f8f8;
    --charcoal:#2a2a2a;
    --grass:#00a651;
    --grass-light:#17b866;
    --grass-deep:#008a43;
    --ink:#1e1e1e;
    --paper-text:#e9e9e9;
  }
  *{margin:0;padding:0;box-sizing:border-box}
  html,body{width:1200px;height:801px;overflow:hidden}
  body{background:var(--stage);position:relative;font-family:"Arimo",Arial,sans-serif}

  .card{position:absolute;width:520px;height:297px;overflow:hidden;box-shadow:0 10px 24px rgba(0,0,0,.18)}

  /* Front card */
  .card-front{left:70px;top:90px;background:var(--card-white)}
  .card-front .swoosh{position:absolute;inset:0}
  .brand-front{position:absolute;left:40px;top:58px;display:flex;align-items:center;gap:12px;white-space:nowrap}
  .brand-dot{width:40px;height:40px;border-radius:50%;background:var(--grass);flex:none}
  .brand-front .brand-name{font-family:"Kaushan Script",cursive;font-size:34px;color:var(--ink);line-height:1}

  .contact-block{position:absolute;right:16px;top:222px;display:flex;align-items:center;gap:12px;white-space:nowrap}
  .person{text-align:right}
  .person-name{font-family:"Kaushan Script",cursive;font-size:19px;color:var(--grass);line-height:1.1}
  .person-role{font-size:12px;color:var(--paper-text);margin-top:2px}
  .divider{width:1px;height:42px;background:var(--paper-text);flex:none}
  .contact-list{list-style:none;font-size:12.5px;color:var(--paper-text)}
  .contact-list li{display:flex;align-items:center;gap:6px;line-height:21px}
  .icon{width:12px;height:12px;flex:none}
  .icon-square{background:var(--grass);border-radius:2px}

  /* Back card */
  .card-back{left:610px;top:410px;background:radial-gradient(ellipse at 35% 45%,var(--grass-light) 0%,var(--grass) 45%,var(--grass-deep) 100%)}
  .brand-back{position:absolute;left:0;right:0;top:88px;display:flex;justify-content:center;align-items:center;gap:16px;white-space:nowrap}
  .brand-back .brand-dot{background:#fff;width:50px;height:50px}
  .brand-back .brand-name{font-family:"Kaushan Script",cursive;font-size:42px;color:#fff;line-height:1}
  .product-line{position:absolute;left:0;right:0;bottom:50px;display:flex;justify-content:center;gap:12px;list-style:none;font-weight:700;font-size:13.5px;color:#e8f7ee;white-space:nowrap}
  .product-line li::before{content:"•";margin-right:5px}
</style>
</head>
<body>

<section class="card card-front" aria-label="Business card front">
  <svg class="swoosh" viewBox="0 0 520 297" width="520" height="297" aria-hidden="true">
    <path d="M150 297 C125 235 200 200 320 160 C420 128 478 85 462 0 L520 0 L520 297 Z" fill="var(--charcoal)"/>
    <path d="M128 280 C120 220 190 185 300 148 C380 122 430 100 445 70 C430 108 385 132 310 158 C205 195 140 225 128 280 Z" fill="var(--grass)"/>
  </svg>

  <div class="brand-front">
    <span class="brand-dot"></span>
    <span class="brand-name">Birchwood Clover</span>
  </div>

  <div class="contact-block">
    <div class="person">
      <div class="person-name">Daniel Hargrove</div>
      <div class="person-role">Manager</div>
    </div>
    <span class="divider"></span>
    <ul class="contact-list">
      <li>
        <svg class="icon" viewBox="0 0 24 24" aria-hidden="true"><path fill="var(--grass)" d="M6.6 10.8a15 15 0 0 0 6.6 6.6l2.2-2.2a1 1 0 0 1 1-.25 11.4 11.4 0 0 0 3.6.57 1 1 0 0 1 1 1V20a1 1 0 0 1-1 1A17 17 0 0 1 3 4a1 1 0 0 1 1-1h3.5a1 1 0 0 1 1 1c0 1.25.2 2.45.57 3.570a1 1 0 0 1-.25 1z"/></svg>
        555-218-3946
      </li>
      <li><span class="icon icon-square"></span>@birchwoodclover</li>
    </ul>
  </div>
</section>

<section class="card card-back" aria-label="Business card back">
  <div class="brand-back">
    <span class="brand-dot"></span>
    <span class="brand-name">Birchwood Clover</span>
  </div>
  <ul class="product-line">
    <li>Orchardgrass Hay</li>
    <li>Alfalfa Hay</li>
    <li>Mixed Grass Hay</li>
    <li>Premium Quality Hay</li>
  </ul>
</section>

</body>
</html>
```